Local fast-growing company in the service sector

We are looking for a modern business card design, which should also appear on our letterheads

Target Market(s)

Private and industrial sectors

Contact Information for Business Card

Vorname Name
Kellbacher Str. 38
74819 Fellbrunn
Tel.: 07162-418395-0
Name@service-tkwl.de

Colors
9d9d9d
919191
aaaaaa

Requirements
Must have
• The logo (file) in silver

```html
<!DOCTYPE html>
<html lang="de">
<head>
<meta charset="utf-8">
<title>TKWL Visitenkarte</title>
<link rel="stylesheet" href="https://fonts.googleapis.com/css2?family=Work+Sans:wght@400;500;600&display=swap">
<style>
  :root {
    --stage: #2a2a2a;
    --card: #9d9d9d;
    --card-dark: #919191;
    --band: #aaaaaa;
    --ink: #ffffff;
    --ink-soft: #eeeeee;
    --mark: #d9d9d9;
  }
  * { box-sizing: border-box; margin: 0; padding: 0; }
  html, body { width: 1200px; height: 900px; overflow: hidden; }
  body {
    background: var(--stage);
    font-family: "Work Sans", Arial, sans-serif;
    color: var(--ink);
    position: relative;
  }
  .card {
    position: absolute;
    width: 580px;
    height: 331px;
    background: var(--card);
    box-shadow: 0 10px 30px rgba(0,0,0,.45);
    overflow: hidden;
  }
  .card--front { left: 310px; top: 60px; }
  .card--back { left: 310px; top: 470px; }

  .brand { position: absolute; display: flex; align-items: center; gap: 14px; }
  .brand__square { width: 42px; height: 42px; background: var(--mark); }
  .brand__text { display: flex; flex-direction: column; }
  .brand__name {
    font-weight: 600; font-size: 54px; line-height: 1; letter-spacing: 2px; color: var(--mark);
  }
  .brand__web {
    font-weight: 600; font-size: 17px; letter-spacing: 1.5px; color: var(--mark); margin-top: 4px;
  }
  .card--front .brand { left: 160px; top: 118px; }
  .card--back .brand { left: 340px; top: 95px; }
  .card--back .brand__name { font-size: 46px; }
  .card--back .brand__web { font-size: 15px; }

  .name-band {
    position: absolute; left: 0; top: 24px; width: 340px; height: 72px;
    background: var(--band); padding: 12px 0 0 24px;
  }
  .person__name { font-weight: 500; font-size: 24px; letter-spacing: .5px; line-height: 1.05; }
  .person__role { font-weight: 400; font-size: 12px; letter-spacing: 1px; color: var(--ink-soft); margin-top: 4px; }

  .contact { position: absolute; left: 24px; bottom: 28px; list-style: none; }
  .contact li {
    display: flex; align-items: center; gap: 10px;
    font-size: 15px; line-height: 23px; letter-spacing: .4px;
  }
  .contact svg { width: 12px; height: 12px; fill: var(--ink); flex: none; }

  .address {
    position: absolute; right: 26px; bottom: 28px;
    font-size: 15px; line-height: 22px; letter-spacing: .6px; font-style: normal;
  }
</style>
</head>
<body>

<section class="card card--front" aria-label="Kartenvorderseite">
  <div class="brand">
    <span class="brand__square"></span>
    <div class="brand__text">
      <span class="brand__name">TKWL</span>
      <span class="brand__web">service-tkwl.de</span>
    </div>
  </div>
</section>

<section class="card card--back" aria-label="Kartenrückseite">
  <div class="name-band">
    <p class="person__name">MARVIN KESSLER</p>
    <p class="person__role">DIRECTOR</p>
  </div>

  <div class="brand">
    <span class="brand__square"></span>
    <div class="brand__text">
      <span class="brand__name">TKWL</span>
      <span class="brand__web">service-tkwl.de</span>
    </div>
  </div>

  <ul class="contact">
    <li>
      <svg viewBox="0 0 12 12" aria-hidden="true"><path d="M2.5 0.5l2 2.3-1 1.2a6.5 6.5 0 0 0 4.5 4.5l1.2-1 2.3 2-1.3 2A9.5 9.5 0 0 1 0.5 1.8z"/></svg>
      07162-418395-0
    </li>
    <li>
      <svg viewBox="0 0 12 12" aria-hidden="true"><path d="M3 0h6v12H3zM4 1.5v8h4v-8z"/></svg>
      0152-63947210
    </li>
    <li>
      <svg viewBox="0 0 12 12" aria-hidden="true"><path d="M3 0h6v4H3zM0 4.5h12V12H0zM2 6v1.5h2V6zm3 0v1.5h2V6zm3 0v1.5h2V6zM2 9v1.5h2V9zm3 0v1.5h2V9zm3 0v1.5h2V9z"/></svg>
      07162-418395-9
    </li>
    <li>
      <svg viewBox="0 0 12 12" aria-hidden="true"><path d="M0 2h12v8H0zm1 1v.3l5 3.4 5-3.4V3zm0 1.5V9h10V4.5L6 8z"/></svg>
      Name@service-tkwl.de
    </li>
  </ul>

  <address class="address">
    Kellbacher Str. 38<br>
    74819 Fellbrunn
  </address>
</section>

</body>
</html>
```